cartNest - a stylish trolley for apartments

We neede a simple website to sell our Trolley, for apartment use.
The colour theme is red, blask & white. Our logo is attached and this needs to be on the Home page.
The website only needs a Home Page plus 4 other pges.
In the attachment you will find a site map.

You can check out the following two sites to see what I like:
www.plinvex.example/design-showcase-inspiration/minimalist-portfolio-website/
www.brostaquill.example/inspiration/40-beautiful-web-design-portfolios/ in this site especially
Dario Pesqueta
Q L Smithy
Nine 86 Studio
Albert Crisp

And especially Lamp - I ike the simpicity of the site esp as we are only selling one product

Target Market(s)

Apartment dwellers

Industry/Entity Type

Apartment

Requirements
Must have
• This website must have 4 pages.
We need Zanto, Fundline and Quibpay portals.
Order Form for Trolley
Payment form.

```html
<!DOCTYPE html>
<html lang="en">
<head>
<meta charset="utf-8">
<title>cartNest — Home</title>
<link href="https://fonts.googleapis.com/css2?family=Noto+Sans:ital,wght@0,400;0,700;1,400&family=Tinos:wght@400;700&display=swap" rel="stylesheet">
<style>
  :root{
    --red:#c4161c;
    --red-dark:#a50f15;
    --black:#0d0d0d;
    --ink:#222;
    --grey-text:#8a8a8a;
    --grey-btn:#d9d9d9;
    --line:#d4d4d4;
    --bg:#efefef;
    --link-blue:#1a73c8;
    --caption:rgba(60,60,60,.88);
  }
  *{box-sizing:border-box;margin:0;padding:0}
  html,body{width:1200px;height:1200px;overflow:hidden}
  body{position:relative;background:radial-gradient(ellipse at 50% 40%,#f9f9f9 0%,var(--bg) 70%,#e6e6e6 100%);font-family:"Noto Sans",sans-serif;color:var(--ink)}
  .abs{position:absolute}
  a{text-decoration:none;color:inherit}

  .topbar{left:0;top:0;width:1200px;height:30px;background:var(--black);color:#fff;font-size:12px}
  .topbar .account-links{left:201px;top:7px;letter-spacing:.1px}
  .topbar .account-links span{margin:0 6px}
  .currency-label{left:754px;top:7px;color:#e0242b;font-size:12px}
  .currency-select{left:882px;top:5px;width:118px;height:20px;background:#fff;color:#555;font-size:10px;padding:4px 7px}
  .currency-select svg{position:absolute;right:6px;top:6px}

  .brand{left:500px;top:40px;width:200px;height:105px;text-align:center}
  .brand-mark{position:absolute;left:88px;top:10px;width:24px;height:24px;background:var(--red)}
  .brand-name{position:absolute;left:0;top:76px;width:200px;font-size:22px;font-weight:700;color:var(--red)}

  .cart-summary{left:889px;top:89px;font-size:14px;color:var(--red)}
  .cart-summary small{font-size:11px;color:var(--grey-text);margin-left:8px}
  .cart-summary svg{vertical-align:-3px;margin-right:8px}
  .follow{left:856px;top:120px;font-size:12px;color:#777}
  .social{display:inline-block;width:17px;height:17px;background:#8a8a8a;margin-left:3px;vertical-align:-4px}

  .rule{left:200px;width:800px;height:3px;border-top:1px solid var(--line);border-bottom:1px solid var(--line)}
  .main-nav{left:0;top:157px;width:1200px;height:24px}
  .nav-btn{position:absolute;top:0;width:81px;height:24px;background:var(--grey-btn);font-family:"Tinos",serif;font-size:13px;text-align:center;line-height:24px;color:#222}
  .nav-btn.active{background:var(--red);color:#fff}

  .slider{left:200px;top:210px;width:800px;height:261px;border:1px solid #ccc;background:#fff;padding:3px}
  .slider-bg{width:100%;height:100%;background:linear-gradient(90deg,#e8e2dc,#ece9e6 50%,#e4ddd6)}
  .slide{position:absolute;width:227px;height:195px;border:1px solid #fff}
  .slide .photo{width:100%;height:100%}
  .slide .cap{position:absolute;left:0;width:100%;height:38px;background:var(--caption);color:#fff;font-size:10.5px;line-height:14px;padding:4px 7px}

  .section-title{font-size:16.5px;color:#444}
  .section-title b{color:var(--red)}
  .section-title .strong{color:#222;font-weight:700}
  .info-icon{left:212px;top:512px;font-family:"Tinos",serif;font-style:italic;font-weight:700;font-size:26px;color:var(--red)}
  .lead{font-size:10.5px;font-style:italic;line-height:15px;color:#222}
  .body-text{font-size:10.5px;line-height:14.5px;color:var(--grey-text)}
  .more{color:var(--red)}

  .pay-box{left:779px;top:597px;width:213px;height:69px;border:1px solid #c9c9c9;background:#fff}
  .pay-box span{position:absolute;font-size:12px;font-weight:700;color:#333}

  .feature{position:absolute;top:708px;width:228px}
  .feature .photo{width:228px;height:108px}
  .feature .lead{margin-top:22px}
  .feature .body-text{margin-top:6px}

  .thumb{position:absolute;top:977px;width:153px;height:138px;border:3px solid #fff;box-shadow:0 0 2px #bbb}
  .arrow{top:1036px;font-size:26px;color:var(--red-dark);font-family:"Tinos",serif}

  .contact{left:772px;top:975px;width:230px}
  .contact p{font-size:10.5px;font-style:italic;margin-top:9px}
  .contact p a{color:var(--link-blue)}

  .footer{left:0;top:1163px;width:1200px;height:37px;background:var(--black);color:#fff;font-family:"Tinos",serif;font-size:13px}
  .footer span{position:absolute;top:10px}
  .footer .foot-brand{color:var(--red);font-family:"Noto Sans",sans-serif;font-weight:700;font-size:13px}
</style>
</head>
<body>

<header>
  <div class="abs topbar">
    <nav class="abs account-links"><a>My Account</a><span>|</span><a>My Cart</a><span>|</span><a>Checkout</a><span>|</span><a>Log In</a></nav>
    <div class="abs currency-label">Select Your Currency</div>
    <div class="abs currency-select">US Dollar - USD
      <svg width="10" height="7" viewBox="0 0 10 7"><path d="M0 0h10L5 7z" fill="#222"/></svg>
    </div>
  </div>

  <div class="abs brand"><div class="brand-mark"></div><div class="brand-name">cartNest</div></div>

  <div class="abs cart-summary">
    <svg width="20" height="17" viewBox="0 0 20 17"><path d="M0 2h4l3 9h10l2-6H6" fill="none" stroke="#333" stroke-width="1.6"/><circle cx="8" cy="14.5" r="1.6" fill="#333"/><circle cx="16" cy="14.5" r="1.6" fill="#333"/></svg>Cart:<small>(empty)</small>
  </div>
  <div class="abs follow">Follow us on :<span class="social" style="margin-left:6px"></span><span class="social"></span><span class="social"></span></div>

  <div class="abs rule" style="top:148px"></div>
  <nav class="abs main-nav">
    <a class="nav-btn active" style="left:338px">cartNest</a>
    <a class="nav-btn" style="left:451px">Gallery</a>
    <a class="nav-btn" style="left:562px">Contact Us</a>
    <a class="nav-btn" style="left:675px">Cart</a>
    <a class="nav-btn" style="left:787px">Payment</a>
  </nav>
  <div class="abs rule" style="top:185px"></div>
</header>

<main>
  <section class="abs slider">
    <div class="slider-bg" role="img" aria-label="Blurred interior backdrop behind the slides"></div>
    <figure class="slide" style="left:29px;top:25px">
      <div class="photo" role="img" aria-label="Trolley with red luggage in an apartment hallway" style="background:linear-gradient(135deg,#8a5a3a,#3a3c44 50%,#b07040)"></div>
      <figcaption class="cap" style="top:156px">Lorem Ipsum is simply dummy text of the printing and typesetting industry.</figcaption>
    </figure>
    <figure class="slide" style="left:286px;top:42px">
      <div class="photo" role="img" aria-label="Close-up of the chrome trolley frame" style="background:linear-gradient(160deg,#b9cdd2,#9fb7bd 60%,#c7d3d4)"></div>
      <figcaption class="cap" style="top:0">Lorem Ipsum is simply dummy text of the printing and typesetting industry.</figcaption>
    </figure>
    <figure class="slide" style="left:542px;top:24px">
      <div class="photo" role="img" aria-label="Close-up of trolley castor wheels" style="background:linear-gradient(180deg,#8a2a22,#2a2a2a 35%,#cfc2b2 70%,#a87a4a)"></div>
      <figcaption class="cap" style="top:156px">Lorem Ipsum is simply dummy text of the printing and typesetting industry.</figcaption>
    </figure>
  </section>

  <section class="about">
    <div class="abs info-icon">i</div>
    <h2 class="abs section-title" style="left:235px;top:516px">About <b>cart</b><span class="strong">Nest</span></h2>
    <h2 class="abs section-title" style="left:772px;top:516px">Pay by <b>Credit</b> <span class="strong">or</span> <b>Debit</b> <span class="strong">Cards</span></h2>
    <div class="abs" style="left:200px;top:541px;width:800px;border-top:2px solid var(--line)"></div>
    <p class="abs lead" style="left:201px;top:557px;width:510px">cartNest evolved from demand!&nbsp; Apartment dwellers everywhere are calling for a solution to moving shopping, luggage and other goods from car to apartment, and vice versa.</p>
    <p class="abs body-text" style="left:201px;top:593px;width:510px">cartNest evolved from demand!&nbsp; Apartment dwellers everywhere are calling for a solution to moving shopping, luggage and other goods from car to apartment, and vice versa. Other trolleys on the market are not versatile, they are not robust, but more importantly, they are NOT stylish! The emphasis of cartNest is on style. This trolley is stylish enough to remain in your apartment as a piece of furniture. It features a versatile flat-bed and hanger, to cope with all your transport needs. <a class="more">Read More ...</a></p>
    <p class="abs lead" style="left:772px;top:557px">We accept Zanto, Fundline and Quibpay.</p>
    <div class="abs pay-box">
      <span style="left:70px;top:4px;font-size:17px">Quibpay</span>
      <span style="left:12px;top:36px">Zanto</span>
      <span style="left:138px;top:36px">Fundline</span>
    </div>
  </section>

  <section class="features">
    <article class="feature" style="left:201px">
      <div class="photo" role="img" aria-label="Loading the trolley from a car boot in a garage" style="background:linear-gradient(120deg,#7a7a50,#d8d8d0 40%,#5a5440)"></div>
      <p class="lead">Lorem Ipsum is simply dummy text of the printing and typesetting industry.</p>
      <p class="body-text">Lorem Ipsum has been the industry's stan-dard dummy text ever since.Lorem Ipsum has been the industry's standard dummy text ever since. <a class="more">Read More ...</a></p>
    </article>
    <article class="feature" style="left:486px">
      <div class="photo" role="img" aria-label="Trolley handed over beside a parked car" style="background:linear-gradient(120deg,#6a6a48,#d6d6ce 55%,#5a5442)"></div>
      <p class="lead">Lorem Ipsum is simply dummy text of the printing and typesetting industry.</p>
      <p class="body-text">Lorem Ipsum has been the industry's stan-dard dummy text ever since.Lorem Ipsum has been the industry's standard dummy text ever since. <a class="more">Read More ...</a></p>
    </article>
    <article class="feature" style="left:772px">
      <div class="photo" role="img" aria-label="Trolley loaded with bags next to a car" style="background:linear-gradient(120deg,#5a5a44,#c8c4bc 45%,#dcdcd6 70%,#6a6450)"></div>
      <p class="lead">Lorem Ipsum is simply dummy text of the printing and typesetting industry.</p>
      <p class="body-text">Lorem Ipsum has been the industry's stan-dard dummy text ever since.Lorem Ipsum has been the industry's standard dummy text ever since. <a class="more">Read More ...</a></p>
    </article>
  </section>

  <section class="gallery">
    <div class="abs arrow" style="left:199px">&#10094;</div>
    <div class="thumb" style="left:226px" role="img" aria-label="Trolley hanger with garments" style="background:#ccc"><div style="width:100%;height:100%;background:linear-gradient(160deg,#d8d6d0,#b8a890 60%,#8a4a3a)"></div></div>
    <div class="thumb" style="left:395px" role="img" aria-label="Red suitcases on the trolley base"><div style="width:100%;height:100%;background:linear-gradient(90deg,#6a4a3a,#b8322a 40%,#c07040)"></div></div>
    <div class="thumb" style="left:564px" role="img" aria-label="Close-up of a trolley wheel"><div style="width:100%;height:100%;background:linear-gradient(180deg,#4a4844,#d8ccbc 50%,#a06a3a)"></div></div>
    <div class="abs arrow" style="left:728px">&#10095;</div>

    <div class="abs contact">
      <h2 class="section-title">Contact&nbsp; <b>cart</b><span class="strong">Nest</span></h2>
      <p style="margin-top:10px;line-height:15px">Lorem Ipsum is simply dummy text of the printing and typesetting industry.</p>
      <p style="margin-top:14px">E-mail : <a>hello@cartnest.example</a></p>
      <p>Mobile : <a>5550134872</a></p>
      <p>Tel no : <a>5550134872</a></p>
    </div>
  </section>
</main>

<footer class="abs footer">
  <span class="foot-brand" style="left:201px">cartNest</span>
  <span style="left:308px">Gallery</span>
  <span style="left:395px">Contact Us</span>
  <span style="left:500px">Cart</span>
  <span style="left:570px">Payment</span>
  <span style="left:755px">Copyright © All rights are reserved by Compny</span>
</footer>

</body>
</html>
```